Business Card for Yachting Management Company

Need a business card design for a new yachting project management company. Attached is the logo for the company.
Our clients are large yacht owners and captains.
Design must be in the style of the logo. Modern, elegant.

Example of data to show:
Oliver Tennant
Project Manager
(+34) 612 870 334
oliver@quarvel.net
Quarvel Management - Marisol Tower, Office 22 - NDR - Palma de Mallorca

The data above will have to be changed (by me) for the different people in the company over the next years.

Will be printed using CardHarbor (Lustrel Business Cards). They provide these guidelines for the size:
"the actual size of the card is 1050 x 600 pixels. However, the full bleed size is 1083 x 633 pixels, and the safe printing area is 1008 x 558 pixels."

```html
<!DOCTYPE html>
<html lang="en">
<head>
<meta charset="utf-8">
<title>Quarvel Management – Business Card</title>
<link rel="stylesheet" href="https://fonts.googleapis.com/css2?family=Exo+2:wght@600&family=Roboto:wght@400&display=swap">
<style>
  :root {
    --page-bg: #2b2b2c;
    --card-top: #1d1e20;
    --card-bottom: #2a2b2e;
    --brand-blue: #1767b3;
    --band-blue: #1a2633;
    --text-light: #e8e9eb;
    --logo-grey: #5d5e62;
  }
  html, body {
    margin: 0;
    width: 1200px;
    height: 1138px;
    overflow: hidden;
    background: var(--page-bg);
  }
  .card {
    position: absolute;
    left: 274px;
    width: 620px;
    height: 374px;
    border-radius: 16px;
    overflow: hidden;
    background: linear-gradient(160deg, var(--card-top) 0%, var(--card-bottom) 100%);
  }
  .card--front { top: 184px; }
  .card--back { top: 606px; }

  .wordmark {
    position: absolute;
    font-family: "Exo 2", sans-serif;
    font-weight: 600;
    text-transform: uppercase;
    line-height: 1;
    text-align: center;
  }
  .wordmark__name { display: block; }
  .wordmark__sub { display: block; letter-spacing: 0.42em; }

  .card--front .wordmark {
    left: 0; right: 0; top: 116px;
    color: var(--logo-grey);
  }
  .card--front .wordmark__name { font-size: 78px; letter-spacing: 0.04em; }
  .card--front .wordmark__sub { font-size: 22px; margin-top: 18px; padding-left: 0.42em; }

  .accent-band { position: absolute; left: 0; top: 0; }

  .card--back .wordmark {
    left: 42px; top: 236px; width: 200px;
    color: var(--brand-blue);
  }
  .card--back .wordmark__name { font-size: 48px; }
  .card--back .wordmark__sub { font-size: 15px; margin-top: 12px; padding-left: 0.42em; }

  .person {
    position: absolute;
    right: 42px; top: 54px;
    text-align: right;
  }
  .person__name {
    font-family: "Exo 2", sans-serif;
    font-weight: 600;
    font-size: 25px;
    color: var(--brand-blue);
    margin: 0;
    line-height: 1;
    text-transform: uppercase;
  }
  .person__role {
    font-family: Roboto, sans-serif;
    font-size: 17px;
    color: var(--text-light);
    margin: 6px 0 0;
  }

  .contact {
    position: absolute;
    right: 42px; top: 243px;
    font-family: Roboto, sans-serif;
    font-size: 16px;
    color: var(--text-light);
    text-align: right;
    line-height: 24px;
    font-style: normal;
  }
  .contact__line { display: flex; justify-content: flex-end; align-items: center; gap: 8px; }
  .contact__icon { width: 14px; height: 14px; fill: var(--brand-blue); margin-left: 6px; }
  .contact__icon--small { width: 12px; height: 12px; margin: 0 2px; }
  .contact__line--phone { margin-top: 3px; }
</style>
</head>
<body>

<section class="card card--front">
  <div class="wordmark">
    <span class="wordmark__name">Quarvel</span>
    <span class="wordmark__sub">Management</span>
  </div>
</section>

<section class="card card--back">
  <svg class="accent-band" width="620" height="374" viewBox="0 0 620 374" aria-hidden="true">
    <defs>
      <linearGradient id="bandFade" x1="0" y1="0" x2="1" y2="1">
        <stop offset="0" stop-color="#1b2430"/>
        <stop offset="1" stop-color="#1a2a3b"/>
      </linearGradient>
    </defs>
    <polygon points="0,14 6,14 254,374 0,374" fill="url(#bandFade)"/>
  </svg>

  <div class="wordmark">
    <span class="wordmark__name">Quarvel</span>
    <span class="wordmark__sub">Management</span>
  </div>

  <div class="person">
    <h1 class="person__name">Oliver Tennant</h1>
    <p class="person__role">Project Manager</p>
  </div>

  <address class="contact">
    <div class="contact__line">Marisol Tower, Office 22</div>
    <div class="contact__line">NDR - Palma De Mallorca</div>
    <div class="contact__line contact__line--phone">(+34) 612 870 334
      <svg class="contact__icon" viewBox="0 0 16 16" aria-hidden="true"><path d="M2 5c0-2 3-3 6-3s6 1 6 3v1h-3V5H5v1H2zM4 7h8l2 7H2z"/></svg>
    </div>
    <div class="contact__line">quarvel.net
      <svg class="contact__icon contact__icon--small" viewBox="0 0 16 16" aria-hidden="true"><circle cx="8" cy="8" r="7"/></svg>
      oliver@quarvel.net
      <svg class="contact__icon" viewBox="0 0 16 16" aria-hidden="true"><path d="M1 3h14v10H1zM2 4l6 5 6-5" stroke="#1d1e20" stroke-width="1.2"/></svg>
    </div>
  </address>
</section>

</body>
</html>
```